Carlin Hobart

I am a songwriter and would like to include a bio, pictures, discography, CD covers and access to some of my music

Target Market(s)

Music Lovers, songwriters publishers

Coding

Coded - Design and coding required

Number of Pages Required

5+ page

Requirements
Must have
• Pictures of my CD covers, pictures of me and either my Music or links to my music
Nice to have
Should not have
• cartoons

```html
<!DOCTYPE html>
<html lang="en">
<head>
<meta charset="utf-8">
<title>Carlin Hobart – Songwriter</title>
<link href="https://fonts.googleapis.com/css2?family=Montserrat:ital,wght@0,400;0,500;0,600;0,700;1,400&family=Alfa+Slab+One&display=swap" rel="stylesheet">
<style>
:root{
  --navy:#1c1b2e;
  --rust:#7d2a08;
  --yellow:#f7c600;
  --cream:#fff8dc;
  --ink:#222;
  --muted:#777;
  --white:#fff;
}
*{margin:0;padding:0;box-sizing:border-box}
html,body{width:1200px;height:4386px;overflow:hidden}
body{font-family:"Montserrat",sans-serif;color:var(--ink);background:var(--white);position:relative}
section,header,footer{position:absolute;left:0;width:1200px;overflow:hidden}
.abs{position:absolute}

.site-nav{top:0;height:63px;background:var(--navy);color:var(--white)}
.brand{left:60px;top:20px;font-weight:700;font-size:19px}
.menu{right:60px;top:24px;display:flex;gap:26px;font-size:11px;list-style:none}
.menu .active{color:var(--yellow)}
.menu .active::before{content:"";display:inline-block;width:6px;height:6px;border-radius:50%;background:var(--yellow);margin-right:8px;vertical-align:1px}

.hero{top:63px;height:648px;background:radial-gradient(ellipse at 60% 50%,#6b4a32,#3d281b 75%)}
.hero-title{width:100%;text-align:center;top:64px;font-family:"Alfa Slab One",serif;font-size:64px;color:var(--white);letter-spacing:1px}
.hero-tag{width:100%;text-align:center;top:140px;color:var(--yellow);font-size:20px}
.hero-art{left:449px;top:205px;width:300px;height:320px;background:radial-gradient(circle at 50% 52%,#4a2a1a 0%,#3a2418 45%,rgba(61,40,27,0) 70%)}

.about{top:711px;height:533px;background:linear-gradient(90deg,#a8400c 0%,#5c1e05 30%,#1a0a04 55%,#050302 70%)}
.about-photo{left:0;top:0;width:600px;height:533px;background:linear-gradient(180deg,#3a1508 0%,#c2510f 30%,#5a1d06 60%,#2a0d04 100%)}
.about-text{left:645px;top:67px;width:380px;color:#ddd;font-size:11.5px;line-height:19.5px}
.eyebrow{color:var(--yellow);font-size:13px}
.about h2{color:var(--white);font-size:29px;font-weight:600;margin:2px 0 10px}
.underline{position:relative;height:2px;width:90px;background:var(--rust)}
.underline::after{content:"";position:absolute;left:50%;top:-3px;width:8px;height:8px;border-radius:50%;background:var(--rust);transform:translateX(-50%)}
.about p{margin-top:16px}
.btn{display:inline-block;background:var(--rust);color:var(--white);font-weight:600;font-size:13px;border-radius:20px;padding:10px 22px;text-transform:uppercase}

.sec-title{width:100%;text-align:center;font-size:29px;font-weight:600}
.sec-title .underline{margin:8px auto 0}

.music{top:1244px;height:919px}
.track{display:flex;border:1px solid #f2e27a;background:var(--white)}
.track .thumb{width:196px;height:128px;margin:6px;flex:none}
.track .info{flex:1;padding:24px 40px}
.track h3{font-size:17px;font-weight:600}
.track .artist{color:var(--rust);font-size:11px;margin:3px 0 16px}
.track p{font-size:10.5px;color:var(--muted);line-height:18px;width:300px}
.track .play{width:167px;background:var(--cream);display:flex;flex-direction:column;align-items:center;justify-content:center;font-size:12.5px;font-weight:600;gap:18px}
.play-ico{width:48px;height:48px;border-radius:50%;background:var(--rust);position:relative}
.play-ico::after{content:"";position:absolute;left:20px;top:15px;border-left:13px solid var(--white);border-top:9px solid transparent;border-bottom:9px solid transparent}
.track.featured{background:var(--rust);border-color:var(--rust);color:var(--white)}
.track.featured .artist,.track.featured p{color:#f3d9c8}
.track.featured .play{background:var(--yellow);color:var(--white);width:180px}
.track.featured .play-ico{background:var(--white)}
.track.featured .play-ico::after{border-left-color:var(--rust)}
.explore{left:0;width:100%;text-align:center;top:838px;font-size:12px;color:var(--rust);text-decoration:underline}

.reviews{top:2163px;height:509px;background:radial-gradient(ellipse at 50% 40%,#9a3a0c,var(--rust) 70%);color:var(--white)}
.reviews .underline{background:var(--yellow)}
.reviews .underline::after{background:var(--yellow)}
.avatar{left:557px;top:130px;width:86px;height:86px;border-radius:50%;border:3px solid var(--yellow);background:radial-gradient(circle,#d9a36b,#5a2a12)}
.quote{left:262px;top:250px;width:676px;text-align:center;font-style:italic;font-size:11.5px;line-height:21px;color:#f3ddcf}
.reviewer{width:100%;text-align:center;top:398px;font-weight:600;font-size:14px}
.stars{width:100%;text-align:center;top:424px;color:var(--yellow);font-size:18px;letter-spacing:3px}

.disco{top:2672px;height:523px}
.album-art{left:112px;top:77px;width:548px;height:368px;background:linear-gradient(90deg,#c08a4c 0%,#b07a40 60%,#2a2a30 70%,#15151d 100%)}
.disco-text{left:745px;top:88px}
.disco-text h2{font-size:29px;font-weight:600}
.disco-text .underline{margin-top:8px;width:70px}
.disco-text h4{color:var(--yellow);font-size:14px;font-weight:600;margin:30px 0 14px;text-transform:uppercase}
.songs{list-style:none;font-size:11.5px;color:#444}
.songs li{height:27.5px}
.songs li::before{content:"+";color:var(--rust);font-weight:700;font-size:16px;margin:0 14px 0 4px}

.covers{top:3195px;height:476px;background:var(--cream)}
.cover{top:165px;width:240px;height:240px}
.cover .art{width:240px;height:183px}
.cover .label{position:absolute;left:0;top:168px;width:194px;height:67px;background:var(--rust);border-left:4px solid var(--yellow);color:var(--white);font-size:12.5px;font-weight:600;padding:16px;line-height:18px}
.cover:first-of-type .label{background:var(--yellow);color:var(--ink)}

.newsletter{top:3671px;height:409px}
.nl-text{left:231px;top:64px}
.nl-text h2{font-size:29px;font-weight:600;line-height:33px}
.nl-text .underline{margin-left:-25px;margin-top:10px;width:60px}
.nl-text p{font-size:11.5px;color:#444;line-height:20px;margin:24px 0 18px;width:240px}
.field{width:300px;height:36px;border:1px solid #ccc;border-radius:18px;font-size:11px;color:#666;padding:11px 18px;margin-bottom:8px}
.nl-text .btn{padding:10px 24px;margin-top:4px}
.nl-photo{left:686px;top:44px;width:330px;height:330px;border-radius:50%;background:radial-gradient(circle,#b08a6a 0%,#6a4a3a 45%,#141414 62%)}

.site-footer{top:4080px;height:306px;background:var(--navy);color:#ccc;font-size:11px}
.fcol{top:54px}
.fcol h4{color:var(--white);font-size:14px;font-weight:600;margin-bottom:18px}
.fcol.brand-col h4{font-size:20px}
.fcol p{line-height:20px;width:250px}
.read{margin-top:12px;display:block;color:#b63a0c}
.links{list-style:none;line-height:20px}
.links li::before{content:"";display:inline-block;width:4px;height:4px;background:#c0410d;border-radius:50%;margin-right:14px;vertical-align:2px}
.contact-row{display:flex;align-items:center;gap:14px;margin-bottom:14px}
.socials{display:flex;gap:10px}
.socials span{width:32px;height:32px;border-radius:50%;background:#8f2f08;display:block}
.copy{width:100%;text-align:center;top:276px;font-size:10.5px;color:#bbb}
.copy b{color:#c0410d;font-weight:400}
</style>
</head>
<body>

<header class="site-nav">
  <div class="abs brand">Carlin Hobart</div>
  <ul class="abs menu">
    <li class="active">Home</li><li>Bio</li><li>Reviews</li><li>Pictures</li><li>Discography</li><li>CD Covers</li><li>Contact</li>
  </ul>
</header>

<section class="hero" role="img" aria-label="Background photo of a hand writing sheet music">
  <div class="abs hero-title">Carlin Hobart</div>
  <div class="abs hero-tag">{ The Best SONG Writer }</div>
  <div class="abs hero-art" role="img" aria-label="Illustration of a record with music notes around it"></div>
</section>

<section class="about">
  <div class="abs about-photo" role="img" aria-label="Photo of Carlin Hobart standing before a glowing fire crater at night"></div>
  <div class="abs about-text">
    <div class="eyebrow">Welcome To</div>
    <h2>Carlin Hobart</h2>
    <div class="underline" style="margin-left:-15px"></div>
    <p style="margin-top:30px">Carlin Hobart was born and raised in Houston, Texas. He began playing music at the age of eight when his sister returned home from summer camp and asked her parents to buy her a baritone ukulele. She taught her younger brother some chords on the ukulele and he was hooked.</p>
    <p>The following spring, they went to one of the border towns in Mexico and bought a Mexican guitar for $12. They restrung it with nylon strings and Hobart began to learn how to play the guitar.</p>
    <p>He took guitar lessons at a local music store and learned how to play the hits of the day by groups like the Lantern Boys, the Harbor Kings, and the Wrenfields.</p>
    <div class="btn" style="margin-top:14px">Explore More</div>
  </div>
</section>

<section class="music">
  <div class="abs sec-title" style="top:72px">My Music<div class="underline" style="width:62px"></div></div>

  <div class="abs track" style="left:225px;top:158px;width:750px;height:143px">
    <div class="thumb" role="img" aria-label="Album cover: fiery collage with coffee cup" style="background:linear-gradient(135deg,#e8561a,#7a2a0a 60%,#2a2a3a)"></div>
    <div class="info"><h3>Paper Lantern Highway</h3><div class="artist">Rex Calder</div><p>Lorem Ipsum is simply dummy text of the printing and typesetting industry has been the industry.</p></div>
    <div class="play"><span class="play-ico"></span>Play The Music</div>
  </div>

  <div class="abs track featured" style="left:187px;top:322px;width:826px;height:141px">
    <div class="thumb" role="img" aria-label="Album cover: lightning storm over a silhouette" style="background:linear-gradient(135deg,#2a2f55,#8a8fb5 45%,#111)"></div>
    <div class="info"><h3>Restless Weather Blues</h3><div class="artist">Rex Calder</div><p>Lorem Ipsum is simply dummy text of the printing and typesetting industry has been the industry.</p></div>
    <div class="play"><span class="play-ico"></span>Play The Music</div>
  </div>

  <div class="abs track" style="left:225px;top:487px;width:750px;height:143px">
    <div class="thumb" role="img" aria-label="Album cover: ship on stormy waves" style="background:linear-gradient(180deg,#3a4a5a,#6a8090 50%,#1e2a30)"></div>
    <div class="info"><h3>When The Tide Turns Home</h3><div class="artist">Carlin Hobart</div><p>Lorem Ipsum is simply dummy text of the printing and typesetting industry has been the industry.</p></div>
    <div class="play"><span class="play-ico"></span>Play The Music</div>
  </div>

  <div class="abs track" style="left:225px;top:651px;width:750px;height:143px">
    <div class="thumb" role="img" aria-label="Album cover: childhood photo collage" style="background:linear-gradient(135deg,#dfe6f0,#b7c4d8 50%,#e8d9c8)"></div>
    <div class="info"><h3>Back When I Was Small</h3><div class="artist">Carlin Hobart</div><p>Lorem Ipsum is simply dummy text of the printing and typesetting industry has been the industry.</p></div>
    <div class="play"><span class="play-ico"></span>Play The Music</div>
  </div>

  <div class="abs explore">Explore More &nbsp;<svg width="26" height="8" viewBox="0 0 26 8"><path d="M0 4h24M20 1l4 3-4 3" stroke="#7d2a08" fill="none"/></svg></div>
</section>

<section class="reviews">
  <div class="abs sec-title" style="top:66px">Reviews<div class="underline" style="width:62px"></div></div>
  <div class="abs avatar" role="img" aria-label="Reviewer portrait"></div>
  <svg class="abs" style="left:168px;top:282px" width="16" height="40"><path d="M14 2L2 20l12 18" stroke="#fff" fill="none" stroke-width="2"/></svg>
  <svg class="abs" style="left:978px;top:282px" width="16" height="40"><path d="M2 2l12 18L2 38" stroke="#fff" fill="none" stroke-width="2"/></svg>
  <p class="abs quote">" If you are looking for superior wring and song composition then Carlin is your guy. Not only is he truly a professional, He has a unique style and extremely engaging storytelling. I am wowed every time!!! 10 stars! Once again Carlin delivers an AMAZING SONG! I still can't believe how thoughtful and precise Carlin's writing skills are. Phenomenal :) Carlin is a rare breed. His lyrical content and melody selections are superb. He addresses current events via his music with a point of view that really engages you. His musical talents are inspiring. He knows what he is doing point blank period! :) "</p>
  <div class="abs reviewer">Award Nominated Songwriter Vocals</div>
  <div class="abs stars">★★★★★★★★★★</div>
</section>

<section class="disco">
  <div class="abs album-art" role="img" aria-label="Album sleeve with guitarist cover art and a record sliding out"></div>
  <div class="abs disco-text">
    <h2>Discography</h2>
    <div class="underline"></div>
    <h4>Roots Beneath The Pines</h4>
    <ul class="songs">
      <li>Down By The Silver Creek</li>
      <li>The Letter She Might Never Send As Long As You're Around</li>
      <li>A Song Without Verses</li>
      <li>Will The Morning Find Us</li>
    </ul>
    <div class="btn" style="margin-top:4px;padding:10px 24px">View All Discography</div>
  </div>
</section>

<section class="covers">
  <div class="abs sec-title" style="top:72px">CD Cover<div class="underline" style="width:62px"></div></div>
  <div class="abs cover" style="left:87px"><div class="art" role="img" aria-label="CD cover: man with mandolin on colourful background" style="background:linear-gradient(135deg,#e24a8a,#f0a020 50%,#2a6ad0)"></div><div class="label">Old Porch Serenade</div></div>
  <div class="abs cover" style="left:349px"><div class="art" role="img" aria-label="CD cover: ship collage with text" style="background:linear-gradient(135deg,#1e2a6a,#c86a40 60%,#2a1a3a)"></div><div class="label">When The Tide Turns</div></div>
  <div class="abs cover" style="left:611px"><div class="art" role="img" aria-label="CD cover: bright abstract painting" style="background:linear-gradient(135deg,#d02020,#f0c020 40%,#2040c0 75%,#111)"></div><div class="label">Open Doors</div></div>
  <div class="abs cover" style="left:873px"><div class="art" role="img" aria-label="CD cover: sunlit forest" style="background:linear-gradient(180deg,#f4f4ec,#5aa030 40%,#1e4a14)"></div><div class="label">Roots Beneath The Pines</div></div>
</section>

<section class="newsletter">
  <div class="abs nl-text">
    <h2>Sign Up For<br>Newsletter</h2>
    <div class="underline"></div>
    <p>Would you like to receive our exclusive update for Signup !</p>
    <div class="field">Name *</div>
    <div class="field">Email *</div>
    <div class="btn">Subscribe</div>
  </div>
  <div class="abs nl-photo" role="img" aria-label="Photo of Carlin Hobart with a guitar framed in a record"></div>
</section>

<footer class="site-footer">
  <div class="abs fcol brand-col" style="left:60px;top:48px">
    <h4>Carlin Hobart</h4>
    <p>Carlin Hobart was born and raised in Houston, Texas. He began playing music at the age of eight when his sister returned home from summer camp....</p>
    <span class="read">Read More.....</span>
  </div>
  <div class="abs fcol" style="left:337px">
    <h4>Sitemap</h4>
    <ul class="links"><li>Home</li><li>Bio</li><li>Reviews</li><li>Pictures</li><li>Discography</li><li>CD Covers</li><li>Contact</li></ul>
  </div>
  <div class="abs fcol" style="left:614px">
    <h4>Contact Us</h4>
    <div class="contact-row"><svg width="14" height="14" viewBox="0 0 24 24"><path d="M6 2l4 5-2 3c1 3 3 5 6 6l3-2 5 4-3 4C10 22 2 14 2 5z" fill="#c0410d"/></svg>+1 555 014 2290</div>
    <div class="contact-row"><svg width="14" height="12" viewBox="0 0 24 18"><rect x="1" y="1" width="22" height="16" fill="none" stroke="#c0410d" stroke-width="2"/><path d="M1 1l11 9 11-9" fill="none" stroke="#c0410d" stroke-width="2"/></svg>mail@hobartsongs.com</div>
  </div>
  <div class="abs fcol" style="left:892px">
    <h4>Follow Us</h4>
    <div class="socials"><span aria-label="Social link 1"></span><span aria-label="Social link 2"></span><span aria-label="Social link 3"></span></div>
  </div>
  <div class="abs copy">©<b>Carlin Hobart</b> - 2020 All rights reserved.</div>
</footer>

</body>
</html>
```